HOLLOWMERE RESTASURANT WINE LIST - REDESIGN/REFORMAT

Need a menu redesign/resizing of our wine list/beverage menu from standard letter size to a 4.25 x 11 inch “Drink Menu” size. Could do with a nicer cover page. Wine list, descriptions, pricing, almost all stays the same minus the formatting and possibly new cover page/font.

Few minor edits need to be made to descriptions and pricing on wine and beer list.

Someone competent in illustrator should be able to get this done in literal hours, and I don’t find myself having the time, and less know how than someone here!

Need sent back in PDF Format so i can send to local print shop.

Thanks in advance

Our restaurants's customers/patrons

• A few text edits sent in before final edit. please PM so i can tell you what aspects of the wine list/beer menu need to be edited.
• Elegant font but readable

```html
<!DOCTYPE html>
<html lang="en">
<head>
<meta charset="utf-8">
<title>Hollowmere Restaurant – Wine List</title>
<link href="https://fonts.googleapis.com/css2?family=Gelasio:ital,wght@0,400;0,600;1,400;1,600&family=Marcellus&family=Montserrat:wght@800&display=swap" rel="stylesheet">
<style>
:root{
  --page:#ececec;
  --panel:#ffffff;
  --ink:#1a1a1a;
  --soft:#333333;
  --rule:#9a9a9a;
  --mist-top:#ffffff;
  --mist-mid:#e6e6e6;
  --mist-low:#cfcfcf;
}
*{margin:0;padding:0;box-sizing:border-box}
html,body{width:1200px;height:769px;overflow:hidden;background:var(--page)}
body{position:relative;font-family:'Gelasio',Georgia,serif;color:var(--ink)}
.panel{position:absolute;top:16px;width:283px;height:732px;background:var(--panel)}
.cover{left:19px}
.reds{left:313px}
.whites{left:606px}
.sakes{left:900px}

/* cover */
.cover-frame{position:absolute;left:14px;top:14px;width:255px;height:718px;border:1px solid var(--rule);border-bottom:none}
.brand{position:absolute;top:66px;left:0;width:100%;text-align:center;font-family:'Marcellus',serif;font-size:23px;line-height:1.05;letter-spacing:.3px;color:var(--soft)}
.cover-title{position:absolute;top:186px;left:0;width:100%;text-align:center;font-family:'Montserrat',sans-serif;font-weight:800;font-size:37px;letter-spacing:.5px;color:#111}
.cover-art{position:absolute;left:0;top:296px;width:100%;height:436px;background:linear-gradient(to bottom,var(--mist-top) 0%,var(--mist-mid) 16%,#f1f1f1 34%,#dedede 60%,var(--mist-low) 100%)}

/* menu panels */
.panel-title{position:absolute;top:44px;left:0;width:100%;text-align:center;font-style:italic;font-weight:600;font-size:20px;line-height:1.15}
.menu{position:absolute;left:16px;right:11px;top:100px;height:548px;display:flex;flex-direction:column;justify-content:space-between}
.sakes .panel-title{top:38px}
.sakes .menu{top:98px;height:538px}
.section-head{display:grid;grid-template-columns:1fr 32px 36px;align-items:end;font-size:9.4px}
.section-name{font-style:italic;font-weight:600;font-size:12px;white-space:nowrap;text-align:left}
.col{text-align:right}
.item{display:grid;grid-template-columns:1fr 32px 36px;margin-top:1px;padding-left:9px}
.item + .item{margin-top:9px}
.wine{grid-column:1;font-size:7.5px;line-height:1.3;white-space:nowrap}
.wine.wide{grid-column:1/3}
.price{text-align:right;font-size:9.6px;line-height:1.15;white-space:nowrap}
.glass{grid-column:2}
.bottle{grid-column:3}
.note{grid-column:1/4;font-style:italic;font-size:6px;line-height:1.4;color:var(--soft);white-space:nowrap}

/* sake panel rows */
.row{display:grid;grid-template-columns:1fr 30px;padding-left:9px;font-size:6.2px;line-height:1.3;margin-top:3px;white-space:nowrap}
.row .price{font-size:9.6px}
.row em,.draft em{font-style:italic;color:var(--soft)}
.subhead{padding-left:9px;font-style:italic;font-weight:600;font-size:7.4px;margin-top:3px}
.head-pair{display:grid;grid-template-columns:1fr 50px 50px;align-items:end}
.head-pair .price{font-size:9.6px}
.head-pair.sub{padding-left:9px;margin-top:4px}
.head-pair.sub .section-name{font-size:7.4px}
.draft{display:grid;grid-template-columns:1fr 50px 62px;padding-left:9px;font-size:6.2px;line-height:1.3;margin-top:3px;white-space:nowrap}
.draft .price{font-size:9.6px}
.draft .price.mid{padding-right:10px}

.footer{position:absolute;left:0;bottom:17px;width:100%;text-align:center;font-size:7.4px;font-weight:600;line-height:1.33}
.footer em{font-style:italic}
</style>
</head>
<body>

<section class="panel cover">
  <div class="cover-frame"></div>
  <div class="brand">HOLLOWMERE<br>RESTAURANT</div>
  <h1 class="cover-title">WINE LIST</h1>
  <div class="cover-art" role="img" aria-label="Pencil-style illustration of a wine bottle and a filled glass on a deck railing overlooking the sea"></div>
</section>

<section class="panel reds">
  <h2 class="panel-title">Red Wines</h2>
  <div class="menu">
    <div class="section">
      <div class="section-head"><span class="section-name">Barbera</span><span class="col">Glass</span><span class="col">Bottle</span></div>
      <div class="item"><span class="wine wide">2023 Castellane - Oak Hollow Ranch<br>- Amador County-California</span><span class="price bottle">$62</span>
        <span class="note">Layer after layer of dark fruits, exotic spices &amp; truffles.<br>Smooth and well balanced.</span></div>
    </div>
    <div class="section">
      <div class="section-head"><span class="section-name">Cabernet Sauvignon</span></div>
      <div class="item"><span class="wine">2022 Daniel Foret-North Coast-California</span><span class="price glass">$11</span><span class="price bottle">$42</span>
        <span class="note">Flavors of dark cherry, vanilla &amp; espresso.<br>Smooth and light tannins.</span></div>
      <div class="item"><span class="wine wide">2021 Fernbrook - Mendocino - California</span><span class="price bottle">$38</span>
        <span class="note">Black cherry &amp; cedar aromas. Balanced oak profile.</span></div>
      <div class="item"><span class="wine wide">2021 Hartwell Brandt - Sonoma Valley - California</span><span class="price bottle">$78</span>
        <span class="note">Aromas of black currant &amp; blueberry laced with vanilla.</span></div>
    </div>
    <div class="section">
      <div class="section-head"><span class="section-name">Merlot</span></div>
      <div class="item"><span class="wine">2022 Linden Vale - Sonoma California</span><span class="price glass">$10</span><span class="price bottle">$38</span>
        <span class="note">Flavors of black cherry, blackberry, and plum.<br>Rich, concentrated, and silky.</span></div>
    </div>
    <div class="section">
      <div class="section-head"><span class="section-name">Pinotage</span></div>
      <div class="item"><span class="wine wide">2013 Opal Ford - Trinidad - California</span><span class="price bottle">$48</span>
        <span class="note">Aromas of black currant &amp; raspberry complement flavors of<br>chocolate &amp; pomegranate.</span></div>
    </div>
    <div class="section">
      <div class="section-head"><span class="section-name">Pinot Noir</span></div>
      <div class="item"><span class="wine">2022 Shell Point - Edna Valley - California</span><span class="price glass">$10</span><span class="price bottle">$38</span>
        <span class="note">Aromas of strawberry &amp; wild raspberries.<br>Smooth &amp; well balanced with creamy &amp; caramel finish.</span></div>
      <div class="item"><span class="wine wide">2023 Calder - Mendocino - California</span><span class="price bottle">$68</span>
        <span class="note">A potpourri of black cherry, raspberry &amp; toasty oak with a balanced tannins.</span></div>
    </div>
    <div class="section">
      <div class="section-head"><span class="section-name">Zinfandel</span></div>
      <div class="item"><span class="wine">2022 Sideshow - Lodi - California</span><span class="price glass">$9</span><span class="price bottle">$34</span>
        <span class="note">Flavors of blackberries, vanilla &amp; cherries. Medium body and smooth finish.</span></div>
      <div class="item"><span class="wine wide">2023 Bellucci - Sonoma County - California</span><span class="price bottle">$46</span>
        <span class="note">Bold blackberry &amp; licorice aromas.<br>Well structured black cherry, smoky pepper &amp; anise flavors.</span></div>
    </div>
    <div class="section">
      <div class="section-head"><span class="section-name">Red Blend</span></div>
      <div class="item"><span class="wine">2022 Riddle Blend - Napa - California</span><span class="price glass">$11</span><span class="price bottle">$42</span>
        <span class="note">A full bodied Syrah</span></div>
      <div class="item"><span class="wine wide">2022 Tall Timber /T.T. Experience</span><span class="price bottle">$48</span>
        <span class="note">Blend of Petite Sirah &amp; Zinfandel.<br>Flavors of blackberry, violet, fig &amp; black prune.</span></div>
    </div>
  </div>
  <p class="footer"><em>Enjoy 50% off bottled wines and sakes every Wednesday.</em><br>Bottle vintage subject to change. Corkage Fee: $15 per bottle<br>For each bottle purchased from our wine list,<br>we will waive one corkage fee.</p>
</section>

<section class="panel whites">
  <h2 class="panel-title">White Wines &amp; Bubbles</h2>
  <div class="menu">
    <div class="section">
      <div class="section-head"><span class="section-name">Chardonnay</span><span class="col">Glass</span><span class="col">Bottle</span></div>
      <div class="item"><span class="wine">2023 Linden Vale - Sonoma - California</span><span class="price glass">$10</span><span class="price bottle">$38</span>
        <span class="note">Pear &amp; green apple with splashes of vanilla &amp; spice.</span></div>
      <div class="item"><span class="wine wide">2023 Peter Lane - Lodi - California</span><span class="price bottle">$44</span>
        <span class="note">Elegant &amp; crisp. Peach &amp; white currant flavors. Creamy finish.</span></div>
    </div>
    <div class="section">
      <div class="section-head"><span class="section-name">Moscato</span></div>
      <div class="item"><span class="wine">2023 Alder - Rogue Valley - Oregon</span><span class="price glass">$9</span><span class="price bottle">$34</span>
        <span class="note">Aromas of white peach, Asian pear, honeysuckle &amp;<br>citrus blossom with crisp acidity. Delicate &amp; delicious.</span></div>
      <div class="item"><span class="wine wide">2021 Moscato D'Asti - Paolo Rinaldi - Italy - 375ml</span><span class="price bottle">$30</span>
        <span class="note">Fragrant fruity bouquet. Musky notes. Light &amp; gentle on the palate.</span></div>
    </div>
    <div class="section">
      <div class="section-head"><span class="section-name">Pinot Grigio</span></div>
      <div class="item"><span class="wine">2023 Venturi - Friuli Grave - Italy</span><span class="price glass">$10</span><span class="price bottle">$38</span>
        <span class="note">Floral notes. Pear and banana flavors. Crisp and delicate.</span></div>
    </div>
    <div class="section">
      <div class="section-head"><span class="section-name">Riesling</span></div>
      <div class="item"><span class="wine">2023 Alder - Rogue Valley - Oregon</span><span class="price glass">$9</span><span class="price bottle">$34</span>
        <span class="note">Aromas of lavender, dried rose petal &amp; green apple with nectarine flavor.<br>Generous texture with a lingering finish.</span></div>
    </div>
    <div class="section">
      <div class="section-head"><span class="section-name">Rosé</span></div>
      <div class="item"><span class="wine">2024 Endless June - Southern Rhone - France</span><span class="price glass">$8</span><span class="price bottle">$30</span>
        <span class="note">Aroma of ripe cherry. Flavors of apricot, vanilla &amp; strawberry.<br>Smooth &amp; Refreshing. Blend of Grenache, Syrah &amp; Clairette.</span></div>
    </div>
    <div class="section">
      <div class="section-head"><span class="section-name">Sauvignon Blanc</span></div>
      <div class="item"><span class="wine">2025 Fernbrook - Redwood Valley - California</span><span class="price glass">$9</span><span class="price bottle">$34</span>
        <span class="note">Pear flavor with a hint of herbs.</span></div>
      <div class="item"><span class="wine wide">2024 Calder - Mendocino - California</span><span class="price bottle">$48</span>
        <span class="note">Citrus note with gooseberry flavor.</span></div>
      <div class="item"><span class="wine wide">2022 Mt. Serene - North Canterbury - New Zealand</span><span class="price bottle">$42</span>
        <span class="note">Flavors of tropical fruits. Pineapple &amp; Guava Aromas. Creamy.</span></div>
    </div>
    <div class="section">
      <div class="section-head"><span class="section-name">Champagnes &amp; Sparkling Wines</span></div>
      <div class="item"><span class="wine">Amore - Prosecco - Brut - Italy</span><span class="price glass">$10</span><span class="price bottle">$38</span>
        <span class="note">Extremely refreshing.<br>Elegant &amp;Fruity with sweet peach &amp; apple flavors.</span></div>
      <div class="item"><span class="wine wide">Henri Vogel - Brut Reserve - Cremant De Alsace- France</span><span class="price bottle">$42</span>
        <span class="note">Blend of Auxerrois &amp; Pinot Blanc. White peach aroma.<br>Flavors of Asian pear, brioche &amp; rich honey.</span></div>
      <div class="item"><span class="wine wide">2017 Opal Ford - Blanc de Blanc - California</span><span class="price bottle">$66</span>
        <span class="note">100% Chardonnay. Flavors of strawberry &amp; kiwi, green apple peel.</span></div>
      <div class="item"><span class="wine wide">2020 Kesselberg - Brut Rosé - Calistoga - California</span><span class="price bottle">$78</span></div>
    </div>
  </div>
  <p class="footer"><em>Enjoy 50% off bottled wines and sakes every Wednesday.</em><br>Bottle vintage subject to change. Corkage Fee: $15 per bottle<br>For each bottle purchased from our wine list,<br>we will waive one corkage fee.</p>
</section>

<section class="panel sakes">
  <h2 class="panel-title">Sakes, Beers,<br>&amp; Non-Alcoholic</h2>
  <div class="menu">
    <div class="section">
      <div class="head-pair"><span class="section-name">House Sake</span><span class="price">Small $5</span><span class="price">Large $10</span></div>
      <div class="head-pair sub"><span class="section-name">Nakama</span><span class="price">Small $6</span><span class="price">Large $12</span></div>
      <div class="row" style="margin-top:0"><em>Sake mixed with sweet plum wine, served hot or cold.</em></div>
    </div>
    <div class="section">
      <div class="head-pair"><span class="section-name">Plum Wine - 1.5 Liter</span><span class="price">Glass</span><span class="price">Bottle</span></div>
      <div class="draft"><span>Umeya<br><em>Fresh sweet taste. Well matured aroma from plum fruit</em></span><span class="price mid">$ 9</span><span class="price">$50</span></div>
    </div>
    <div class="section">
      <div class="section-name">Premium Cold Sakes and Sparking Sake</div>
      <div class="subhead">Small Bottle - 300ml</div>
      <div class="row"><span>Kaze Hana Organic - <em>Full, dry, fruity and balanced.</em></span><span class="price">$14</span></div>
      <div class="row"><span>Kaze Hana Nigori - <em>Unfiltered. sweet and fruity.<br>&nbsp;&nbsp;&nbsp;&nbsp;&nbsp;&nbsp;&nbsp;&nbsp;&nbsp;&nbsp;&nbsp;&nbsp;&nbsp;&nbsp;&nbsp;&nbsp;&nbsp;&nbsp;&nbsp;&nbsp;Mild coconut aftertaste.</em></span><span class="price">$16</span></div>
      <div class="row"><span>Frost Lily Nigori - <em>Unfiltered. Flavors of Honey dew Melon<br>&nbsp;&nbsp;&nbsp;&nbsp;&nbsp;&nbsp;&nbsp;&nbsp;&nbsp;&nbsp;&nbsp;&nbsp;&nbsp;&nbsp;&nbsp;&nbsp;&nbsp;&nbsp;&nbsp;&amp; Pumpkin. Silky N Smooth</em></span><span class="price">$18</span></div>
      <div class="row"><span>Soft Mist Nigori - <em>Unfiltered. Aromas of squash &amp; nuts.<br>&nbsp;&nbsp;&nbsp;&nbsp;&nbsp;&nbsp;&nbsp;&nbsp;&nbsp;&nbsp;&nbsp;&nbsp;&nbsp;&nbsp;&nbsp;&nbsp;&nbsp;&nbsp;&nbsp;&nbsp;&nbsp;&nbsp;&nbsp;&nbsp;&nbsp;&nbsp;&nbsp;&nbsp;Creamy &amp; dry</em></span><span class="price">$30</span></div>
      <div class="row"><span>Quiet Scholar - <em>Gentle flavors of pumpkin &amp; walnut.</em></span><span class="price">$32</span></div>
      <div class="row"><span>Yume Awa Yuzu Sparkling</span><span class="price">$18</span></div>
      <div class="subhead">Large Bottle - 750ml</div>
      <div class="row"><span>Silver Heron - <em>Floral aroma. Silky and smooth.</em></span><span class="price">$32</span></div>
      <div class="row"><span>Morning Dew - <em>Floral aromas with clean flavors of honeydew &amp; lemon.</em></span><span class="price">$70</span></div>
    </div>
    <div class="section">
      <div class="section-name">1.5 Liter Bottle</div>
      <div class="draft"><span>Kaze Hana Nigori<br><em>Sweet and fruity. Mild coconut aftertaste</em></span><span class="price mid">$ 9</span><span class="price">$50</span></div>
    </div>
    <div class="section">
      <div class="section-name">On Draft</div>
      <div class="draft"><span>Kaito Lager, Pale Tide,<br>Twin Forks IPA, Cedar Creek Amber</span><span class="price">$7/pint</span><span class="price">$18/pitcher</span></div>
      <div class="draft"><span>Redwood Cider - <em>“Orchard Days”<br>- 6.9% - crisp &amp; semi dry</em></span><span class="price">$5/glass</span><span class="price">$10/pint</span></div>
    </div>
    <div class="section">
      <div class="section-name">Bottled Beers</div>
      <div class="row"><span>Stellamar</span><span class="price">$5</span></div>
      <div class="row"><span>Brewhaus, Brewhaus Light</span><span class="price">$4</span></div>
      <div class="row"><span>Clearwater Non-Alcoholic</span><span class="price">$4</span></div>
      <div class="row"><span>Hokusei</span><span class="price">$12</span></div>
    </div>
    <div class="section">
      <div class="section-name">Non-Alcoholic Beverages</div>
      <div class="row"><span>Sparkling Mineral Water</span><span class="price">$5</span></div>
      <div class="row"><span>Cola, Diet Cola, Root Beer, Lemon-Lime, Iced Tea <em>free refills</em></span><span class="price">$3</span></div>
      <div class="row"><span>Cherry Fizz, Cola Cherry</span><span class="price">$4.5</span></div>
      <div class="row"><span>Orange Juice, Apple Juice, Cranberry Juice, Lemonade, Half &amp; Half</span><span class="price">$5</span></div>
      <div class="row"><span>Hot Tea - Green Tea, Herbal Tea, Fresh Brewed Coffee</span><span class="price">$3</span></div>
    </div>
  </div>
  <p class="footer"><em>Enjoy 50% off bottled wines and sakes every Wednesday.</em><br>Bottle vintage subject to change. Corkage Fee: $15 per bottle<br>For each bottle purchased from our wine list,<br>we will waive one corkage fee.</p>
</section>

</body>
</html>
```